Velmora Print House gallery website

I need a Website for a gallery with a shopify integration or maybe even better also compatible with squarespace.
the website should have following riders: Künstler, Veranstaltungen, Shop, About Us.
some nice examples for inspiration of the website architecture are:
https://www.trasselhausgalerie.com/
https://www.plovikwerk-gallery.com/de/
https://quendelmoorgalerie.de/
It should be easy for us to make adaptations and fill the website with new content.
Attached there is the CI an logo for the brand.
Target Market(s)
Art Collectors,
Industry/Entity Type
artgallery
Coding
Coded - Design and coding required
Number of Pages Required
3 page
Look and feel

```html
<!DOCTYPE html>
<html lang="en">
<head>
<meta charset="utf-8">
<title>Velmora Print House</title>
<link rel="stylesheet" href="https://fonts.googleapis.com/css2?family=Montserrat:wght@300;400;500;600&family=Roboto:wght@400;500;700&display=swap">
<style>
:root{
  --red:#c0141f;
  --black:#000;
  --ink:#222;
  --grey:#666;
  --light:#f4f4f4;
  --white:#fff;
  --footer:#161616;
  --footer-text:#cfcfcf;
}
*{box-sizing:border-box;margin:0;padding:0}
html,body{width:1200px;height:4285px;overflow:hidden}
body{position:relative;background:var(--white);font-family:"Roboto",Arial,sans-serif;color:var(--ink)}
a{color:inherit;text-decoration:none}

/* header */
.site-header{position:absolute;left:0;top:0;width:1200px;height:86px;background:var(--white);z-index:3}
.brand-tab{position:absolute;left:146px;top:0;width:290px;height:166px;background:var(--white);clip-path:polygon(0 0,100% 0,100% 52%,82% 100%,18% 100%,0 52%);z-index:4}
.brand-name{position:absolute;left:0;width:290px;top:96px;text-align:center;font-family:"Roboto",sans-serif;font-weight:500;font-size:20px;color:var(--ink)}
.main-nav{position:absolute;top:35px;left:502px;display:flex;gap:24px;font-family:"Roboto",sans-serif;font-weight:500;font-size:13px;color:var(--ink)}
.header-icons{position:absolute;top:33px;left:980px;display:flex;gap:12px}

/* hero */
.hero{position:absolute;left:0;top:86px;width:1200px;height:600px;background:linear-gradient(180deg,#5a5552 0%,#6b655f 40%,#4b4540 70%,#2f2a26 100%)}
.hero-title{position:absolute;top:118px;left:0;width:1200px;text-align:center;font-family:"Montserrat",sans-serif;font-weight:300;font-size:40px;color:var(--white);letter-spacing:1px}
.hero-text{position:absolute;top:172px;left:0;width:1200px;text-align:center;font-size:15px;line-height:24px;color:var(--white)}
.btn{position:absolute;display:flex;align-items:center;justify-content:center;gap:8px;font-weight:700;font-size:13px;text-transform:uppercase}
.btn-red{background:var(--red);color:var(--white)}
.hero-btn{left:526px;top:240px;width:150px;height:40px;font-size:14px}
.hero-dots{position:absolute;top:542px;left:564px;display:flex;gap:5px}
.hero-dots span{width:11px;height:11px;border-radius:50%;border:2px solid var(--white)}
.hero-dots span.active{background:var(--red);border-color:var(--red)}

/* events */
.event{position:absolute;height:251px;display:flex}
.event-info{width:200px;height:100%;padding:56px 0 0 21px;color:var(--white)}
.event-info.black{background:var(--black)}
.event-info.red{background:var(--red)}
.event-date{font-size:12px}
.event-title{margin-top:18px;font-weight:500;font-size:15px;line-height:22px}
.event-btn{display:inline-flex;margin-top:18px;height:36px;padding:0 17px;align-items:center;font-size:12px;font-weight:500}
.event-info.black .event-btn{background:var(--red)}
.event-info.red .event-btn{border:1px solid var(--white)}
.event-img{flex:1;height:100%}

/* section heads */
.sec-square{position:absolute;left:590px;width:22px;height:22px;border:2px solid var(--red)}
.sec-title{position:absolute;left:0;width:1200px;text-align:center;font-family:"Montserrat",sans-serif;font-weight:300;font-size:36px;color:var(--ink);letter-spacing:.5px}

/* products */
.product{position:absolute;width:281px}
.product-frame{width:281px;height:281px;border:7px solid var(--black);padding:15px;background:var(--white)}
.product-art{width:100%;height:100%}
.product-cat{margin-top:26px;text-align:center;font-size:12px;color:var(--grey)}
.product-name{margin-top:6px;text-align:center;font-weight:500;font-size:16px;color:var(--black)}
.product-price{margin-top:14px;text-align:center;font-weight:500;font-size:15px;color:var(--red)}

/* about */
.about{position:absolute;left:0;top:2348px;width:1200px;height:448px;background:var(--red)}
.about-img{position:absolute;left:0;top:0;width:600px;height:448px;background:linear-gradient(120deg,#24343f 0%,#3b5f82 30%,#a24a34 55%,#3a2a22 80%,#1c1612 100%)}
.about-title{position:absolute;left:657px;top:72px;font-family:"Montserrat",sans-serif;font-weight:300;font-size:36px;color:var(--white);display:flex;align-items:center;gap:20px}
.about-title i{display:block;width:24px;height:24px;border:2.5px solid var(--white)}
.about-text{position:absolute;left:657px;width:400px;font-size:13px;line-height:21.5px;color:var(--white);text-align:justify}
.about-btn{left:659px;top:331px;width:137px;height:39px;background:var(--white);color:var(--red);font-weight:500;font-size:13px}

/* artists */
.artists{position:absolute;left:0;top:2796px;width:1200px;height:604px;background:var(--light)}
.artist{position:absolute;top:164px;width:210px;height:306px;border:6px solid var(--black);background:var(--white);padding:12px}
.artist-art{width:100%;height:192px}
.artist-avatar{position:absolute;left:67px;top:162px;width:64px;height:64px;border-radius:50%;border:3px solid var(--white)}
.artist-name{position:absolute;left:0;width:198px;top:250px;text-align:center;font-weight:500;font-size:15px;color:var(--black)}

/* newsletter */
.news-title{position:absolute;top:3460px;left:0;width:1200px;text-align:center;font-family:"Montserrat",sans-serif;font-weight:400;font-size:35px;letter-spacing:1px;color:var(--ink)}
.news-line{position:absolute;left:575px;top:3507px;width:50px;height:3px;background:var(--red)}
.news-text{position:absolute;top:3528px;left:0;width:1200px;text-align:center;font-size:13px;line-height:22px;color:var(--grey)}
.news-input{position:absolute;left:391px;top:3608px;width:271px;height:35px;border:1px solid #ccc;padding-left:13px;display:flex;align-items:center;font-size:11px;color:var(--grey)}
.news-btn{left:672px;top:3608px;width:137px;height:35px}

/* follow */
.follow-title{position:absolute;top:3752px;left:0;width:1200px;display:flex;justify-content:center;align-items:center;gap:14px;font-family:"Montserrat",sans-serif;font-weight:400;font-size:36px;color:var(--black)}
.follow-title i{display:block;width:30px;height:30px;border:3px solid var(--red);border-radius:8px}
.feed{position:absolute;top:3827px;left:0;width:1200px;height:177px;display:flex}
.feed div{width:200px;height:177px}

/* footer */
.site-footer{position:absolute;left:0;top:4004px;width:1200px;height:281px;background:var(--footer);color:var(--footer-text)}
.f-col{position:absolute;top:50px}
.f-head{font-weight:500;font-size:15px;color:var(--white);margin-bottom:14px}
.f-list{list-style:none;font-size:11px;line-height:21px;color:var(--white)}
.f-divider{position:absolute;top:45px;width:1px;height:130px;background:#444}
.contact li{display:flex;gap:14px;align-items:flex-start;margin-bottom:6px;line-height:14px}
.contact svg{flex:none;margin-top:1px}
.social li{display:flex;align-items:center;gap:12px;margin-bottom:9px}
.social i{display:block;width:24px;height:24px;border-radius:50%;background:var(--red)}
.f-rule{position:absolute;left:143px;top:224px;width:914px;height:1px;background:#444}
.copyright{position:absolute;top:247px;left:0;width:1200px;text-align:center;font-size:10px;color:var(--white)}
</style>
</head>
<body>

<header class="site-header">
  <nav class="main-nav">
    <a href="#">HOME</a><a href="#">ARTISTS</a><a href="#">EVENTS</a><a href="#">SHOP</a><a href="#">ABOUT US</a><a href="#">CONTACT US</a>
  </nav>
  <div class="header-icons">
    <svg width="16" height="18" viewBox="0 0 16 18" fill="none" stroke="#222" stroke-width="1.6"><circle cx="8" cy="5" r="3.6"/><path d="M1.5 17c0-4 3-6 6.5-6s6.5 2 6.5 6z"/></svg>
    <svg width="17" height="17" viewBox="0 0 17 17" fill="none" stroke="#222" stroke-width="1.8"><circle cx="7" cy="7" r="5.2"/><path d="M11 11l5 5"/></svg>
    <svg width="19" height="17" viewBox="0 0 19 17" fill="none" stroke="#222" stroke-width="1.8"><path d="M9.5 16S1 10.5 1 5.5A4.3 4.3 0 0 1 9.5 3.8 4.3 4.3 0 0 1 18 5.5C18 10.5 9.5 16 9.5 16z"/></svg>
  </div>
</header>
<div class="brand-tab">
  <div class="brand-name">Velmora Print House</div>
</div>

<section class="hero" role="img" aria-label="Gallery corridor with colourful pop art prints on both walls and a bronze sculpture at the end">
  <h1 class="hero-title">VELMORA PRINT HOUSE</h1>
  <p class="hero-text">Lorem ipsum dolor sit amet, consectetur adipiscing elit, sed<br>incididunt ut labore et dolore magna aliqua.</p>
  <a class="btn btn-red hero-btn" href="#">SHOP NOW
    <svg width="14" height="14" viewBox="0 0 14 14"><circle cx="7" cy="7" r="7" fill="#fff"/><path d="M5.5 4l3 3-3 3" stroke="#c0141f" stroke-width="1.8" fill="none"/></svg>
  </a>
  <div class="hero-dots"><span></span><span></span><span class="active"></span><span></span><span></span></div>
</section>

<!-- events -->
<article class="event" style="left:7px;top:692px;width:582px">
  <div class="event-info black"><div class="event-date">05/02/2024 - 06/03/2024</div><div class="event-title">Lorem ipsum dolor sit amet, consectetur</div><a class="event-btn" href="#">Learn More</a></div>
  <div class="event-img" role="img" aria-label="Painting of a golden sunlit lake with reeds" style="background:linear-gradient(135deg,#d9b35a,#f2e6c2 45%,#7a8f5a 80%,#c99c3c)"></div>
</article>
<article class="event" style="left:596px;top:692px;width:599px">
  <div class="event-info black"><div class="event-date">05/02/2024 - 06/03/2024</div><div class="event-title">Lorem ipsum dolor sit amet, consectetur</div><a class="event-btn" href="#">Learn More</a></div>
  <div class="event-img" role="img" aria-label="Painting of a colourful harbour town with boats" style="background:linear-gradient(160deg,#b98a6a,#c44a32 40%,#d9a04a 65%,#4a5a7a)"></div>
</article>
<article class="event" style="left:7px;top:950px;width:582px">
  <div class="event-img" role="img" aria-label="Classical mythological painting with figures and clouds" style="background:linear-gradient(135deg,#8a5a3a,#e8d8c8 45%,#b07a5a 70%,#5a3a2a)"></div>
  <div class="event-info red"><div class="event-date">05/02/2024 - 06/03/2024</div><div class="event-title">Lorem ipsum dolor sit amet, consectetur</div><a class="event-btn" href="#">Learn More</a></div>
</article>
<article class="event" style="left:596px;top:950px;width:599px">
  <div class="event-img" role="img" aria-label="Painting of a canal street with flowers and café tables" style="background:linear-gradient(135deg,#6a5a4a,#9ab0c8 45%,#5a7a9a 70%,#3a4a5a)"></div>
  <div class="event-info black"><div class="event-date">05/02/2024 - 06/03/2024</div><div class="event-title">Lorem ipsum dolor sit amet, consectetur</div><a class="event-btn" href="#">Learn More</a></div>
</article>

<!-- shop -->
<div class="sec-square" style="top:1282px"></div>
<h2 class="sec-title" style="top:1314px">OUR SHOP</h2>

<div class="product" style="left:143px;top:1394px"><div class="product-frame"><div class="product-art" role="img" aria-label="Swirling night sky painting print" style="background:linear-gradient(160deg,#2a4a8a,#5a7ac0 45%,#1e2a4a 80%,#c0a040)"></div></div><div class="product-cat">PRINTS</div><div class="product-name">Lorem ipsum dolor sit amet</div><div class="product-price">€2300</div></div>
<div class="product" style="left:459px;top:1394px"><div class="product-frame"><div class="product-art" role="img" aria-label="Vivid purple and orange autumn street painting print" style="background:linear-gradient(150deg,#6a3ac0,#e0602a 40%,#8a5ad0 70%,#3a6ac0)"></div></div><div class="product-cat">PRINTS</div><div class="product-name">Lorem ipsum dolor sit amet</div><div class="product-price">€2300</div></div>
<div class="product" style="left:775px;top:1394px"><div class="product-frame"><div class="product-art" role="img" aria-label="Colourful expressive dog portrait print" style="background:linear-gradient(135deg,#f4f4f4,#8a5ac0 40%,#e05a5a 60%,#f4f4f4)"></div></div><div class="product-cat">PRINTS</div><div class="product-name">Lorem ipsum dolor sit amet</div><div class="product-price">€2300</div></div>
<div class="product" style="left:143px;top:1810px"><div class="product-frame"><div class="product-art" role="img" aria-label="Sailing ship on stormy sea painting print" style="background:linear-gradient(180deg,#c8d8d0,#d8c8a0 45%,#3a6a7a 70%,#1e3a4a)"></div></div><div class="product-cat">PRINTS</div><div class="product-name">Lorem ipsum dolor sit amet</div><div class="product-price">€2300</div></div>
<div class="product" style="left:459px;top:1810px"><div class="product-frame"><div class="product-art" role="img" aria-label="Rainy city street with clock tower painting print" style="background:linear-gradient(180deg,#c8c0b8,#8a7a6a 50%,#3a3a3a 80%,#b08a5a)"></div></div><div class="product-cat">PRINTS</div><div class="product-name">Lorem ipsum dolor sit amet</div><div class="product-price">€2300</div></div>
<div class="product" style="left:775px;top:1810px"><div class="product-frame"><div class="product-art" role="img" aria-label="Wild flowers with red poppies painting print" style="background:linear-gradient(160deg,#3a6ab0,#4a8a5a 50%,#d04a2a 70%,#2a5a3a)"></div></div><div class="product-cat">PRINTS</div><div class="product-name">Lorem ipsum dolor sit amet</div><div class="product-price">€2300</div></div>

<a class="btn btn-red" href="#" style="left:516px;top:2228px;width:168px;height:38px">VIEW ALL PRODUCT</a>

<!-- about -->
<section class="about">
  <div class="about-img" role="img" aria-label="Artist painting a large colourful abstract canvas in a studio"></div>
  <h2 class="about-title">ABOUT US<i></i></h2>
  <p class="about-text" style="top:141px">Lorem ipsum dolor sit amet, consectetur adipiscing elit, sed do eiusmod tempor incididunt ut labore et dolore magna aliqua. Ut enim ad minim veniam, quis nostrud exercitation ullamco laboris nisi ut aliquip ex ea commodo consequat.</p>
  <p class="about-text" style="top:239px">&nbsp;Duis aute irure dolor in reprehenderit in voluptate velit esse cillum dolore eu fugiat nulla pariatur. Excepteur sint occaecat cupidatat in culpa qui officia deserunt mollit anim id est laborum.</p>
  <a class="btn about-btn" href="#">LEARN MORE</a>
</section>

<!-- artists -->
<section class="artists">
  <div class="sec-square" style="top:60px"></div>
  <h2 class="sec-title" style="top:92px">OUR ARTISTS</h2>
  <div class="artist" style="left:143px"><div class="artist-art" role="img" aria-label="Painting of a stag" style="background:linear-gradient(160deg,#9aa8a0,#8a5a3a 50%,#5a6a5a)"></div><div class="artist-avatar" role="img" aria-label="Artist portrait" style="background:#5a7aa0"></div><div class="artist-name">MIRA KESSLING</div></div>
  <div class="artist" style="left:378px"><div class="artist-art" role="img" aria-label="Painting of galloping horses" style="background:linear-gradient(150deg,#c0a050,#e8e0c8 50%,#a07a3a)"></div><div class="artist-avatar" role="img" aria-label="Artist portrait" style="background:#6a6a6a"></div><div class="artist-name">MIRA KESSLING</div></div>
  <div class="artist" style="left:611px"><div class="artist-art" role="img" aria-label="Baroque ceiling fresco painting" style="background:radial-gradient(circle at 50% 45%,#a8c8e8,#d89a6a 60%,#8a5a3a)"></div><div class="artist-avatar" role="img" aria-label="Artist portrait" style="background:#e8b8a0"></div><div class="artist-name">MIRA KESSLING</div></div>
  <div class="artist" style="left:845px"><div class="artist-art" role="img" aria-label="Painting of a sailing ship in blue waves" style="background:linear-gradient(170deg,#d8e0e8,#9ab0c8 50%,#3a5a8a)"></div><div class="artist-avatar" role="img" aria-label="Artist portrait" style="background:#4a4a4a"></div><div class="artist-name">MIRA KESSLING</div></div>
  <a class="btn btn-red" href="#" style="left:516px;top:509px;width:168px;height:38px">VIEW ALL ARTISTS</a>
</section>

<!-- newsletter -->
<h2 class="news-title">SUBSCRIBE TO OUR NEWSLETTER</h2>
<div class="news-line"></div>
<p class="news-text">With our newsletter you won't miss any exhibitions. You will also receive special offers and<br>always receive the latest news.</p>
<div class="news-input">Email Address</div>
<a class="btn btn-red news-btn" href="#">SUBMIT NOW</a>

<!-- follow -->
<h2 class="follow-title"><i></i>FOLLOW US</h2>
<div class="feed">
  <div role="img" aria-label="Poppies painting" style="background:linear-gradient(160deg,#3a6ab0,#4a8a5a 55%,#d04a2a)"></div>
  <div role="img" aria-label="Colourful harbour painting" style="background:linear-gradient(160deg,#5a9ad0,#e0a0c0 50%,#3a6ab0)"></div>
  <div role="img" aria-label="Venice canal painting" style="background:linear-gradient(160deg,#d8c090,#b05a3a 50%,#5a8a9a)"></div>
  <div role="img" aria-label="Daisies painting" style="background:linear-gradient(160deg,#8a7a5a,#e8e0c0 50%,#5a6a3a)"></div>
  <div role="img" aria-label="Colourful horse heads painting" style="background:linear-gradient(135deg,#1a1a2a,#2a6ab0 40%,#e04a2a 65%,#1a1a2a)"></div>
  <div role="img" aria-label="Vivid abstract flowers painting" style="background:linear-gradient(135deg,#e04ab0,#f0e0f0 45%,#e06a2a 70%,#8a4ad0)"></div>
</div>

<!-- footer -->
<footer class="site-footer">
  <div class="f-col" style="left:145px"><div class="f-head">QUICK LINKS</div>
    <ul class="f-list"><li>Home</li><li>Artists</li><li>Events</li><li>Shop</li><li>About Us</li></ul></div>
  <div class="f-divider" style="left:291px"></div>
  <div class="f-col" style="left:365px"><div class="f-head">INFORMATION</div>
    <ul class="f-list"><li>Terms &amp; Conditions</li><li>Privacy Policy</li><li>Disclaimer</li><li>Site Map</li><li>Contact Us</li><li>Categories</li></ul></div>
  <div class="f-divider" style="left:539px"></div>
  <div class="f-col" style="left:613px"><div class="f-head">CONTACT INFO</div>
    <ul class="f-list contact">
      <li><svg width="12" height="12" viewBox="0 0 12 12" fill="#c0141f"><path d="M2.5 1l2 2.5-1 1.5a7 7 0 0 0 3.5 3.5l1.5-1L11 9.5 9.5 11C5 11 1 7 1 2.5z"/></svg>(215) 555-0142</li>
      <li><svg width="12" height="12" viewBox="0 0 12 12" fill="#c0141f"><rect x="1" y="4" width="10" height="6"/><rect x="3" y="1" width="6" height="3"/></svg>(215) 555-0142</li>
      <li><svg width="12" height="12" viewBox="0 0 12 12" fill="#c0141f"><rect x="1" y="2.5" width="10" height="7"/></svg><u>info@velmoraprint.com</u></li>
      <li><svg width="12" height="12" viewBox="0 0 12 12" fill="#c0141f"><path d="M6 11S2 6.5 2 4.2a4 4 0 0 1 8 0C10 6.5 6 11 6 11z"/></svg><span>#2868 Lorem ipsum dolor sit<br>amet, consectetur</span></li>
    </ul></div>
  <div class="f-divider" style="left:855px"></div>
  <div class="f-col" style="left:929px"><div class="f-head">FOLLOW US</div>
    <ul class="f-list social"><li><i></i>Pageboard</li><li><i></i>Chirpline</li><li><i></i>Circlenet</li><li><i></i>Workweave</li></ul></div>
  <div class="f-rule"></div>
  <div class="copyright">Copyrights © The Company name 2024 | Allrights Reserved</div>
</footer>

</body>
</html>
```